Tova Brisk Fitness Coaching Project

I am a personal trainer based in London. My services include one-on-one PT sessions, bootcamps.
I would like the design to be minimalistic. With light colours: white, pink, purple.
I specialise in weight loss, flexibility, mobility.

Tova Penrick
Personal Trainer
Email: tova.penrick@mailgrove.net
tel: 07500 918 243
snapgrid: Tova Brisk

Target Market(s)

adults, mostly females (age 18-50).

Industry/Entity Type

Fitness

Contact Information for Business Card

Tova Penrick
Personal Trainer
tel: 07500 918 243
snapgrid: Tova Brisk

Font styles to use
Serif

Colors
eea4c8
fbd4d5
fdf9cf
cfeae6
cee9f5

Requirements
Nice to have
• minimalistic style
• easy to read and remember

```html
<!DOCTYPE html>
<html lang="en">
<head>
<meta charset="utf-8">
<title>Tova Brisk Fitness Coaching – Business Card</title>
<link rel="stylesheet" href="https://fonts.googleapis.com/css2?family=Crimson+Text:wght@400&display=swap">
<style>
  :root {
    --bg: #e2e3e4;
    --card: #ffffff;
    --ink: #1d1d1f;
    --pink: #f2b3f2;
    --pink-name: #ec9fcf;
    --mint: #d3ebe7;
    --photo-warm: #c98a6a;
    --photo-dark: #3b2a24;
    --shadow: rgba(0,0,0,0.16);
  }
  * { margin: 0; padding: 0; box-sizing: border-box; }
  html, body { width: 1200px; height: 1000px; overflow: hidden; background: var(--bg); }
  .stage { position: relative; width: 1200px; height: 1000px; }

  .card {
    position: absolute;
    left: 320px;
    width: 560px;
    height: 320px;
    background: var(--card);
    border-radius: 22px;
    overflow: hidden;
    box-shadow: 0 10px 28px var(--shadow);
  }
  .card--front { top: 140px; }
  .card--back { top: 540px; }

  /* Front */
  .front-band {
    position: absolute; left: 0; right: 0; bottom: 0; height: 30px;
    background: var(--mint);
  }
  .brand {
    position: absolute; left: 44px; top: 108px;
    font-family: "Crimson Text", serif;
    font-weight: 400;
    color: var(--ink);
  }
  .brand__name {
    font-size: 27px;
    line-height: 32px;
    font-weight: 400;
  }
  .brand__role {
    font-size: 18px;
    line-height: 24px;
    margin-top: 6px;
  }
  .action-photo {
    position: absolute; right: 40px; top: 30px;
    width: 210px; height: 170px;
    border-radius: 10px;
    background: linear-gradient(160deg, #f08ab8 0%, #f6c6dc 45%, #3a4550 100%);
    opacity: 0.85;
  }

  /* Back */
  .back-shapes { position: absolute; inset: 0; }
  .portrait {
    position: absolute; left: 40px; top: 112px;
    width: 92px; height: 92px; border-radius: 50%;
    background: radial-gradient(circle at 50% 45%, var(--photo-warm) 0%, var(--photo-dark) 80%);
  }
  .identity { position: absolute; left: 150px; top: 102px; font-family: "Crimson Text", serif; }
  .identity__name { font-size: 28px; color: var(--pink-name); font-weight: 400; line-height: 1.1; }
  .identity__role { font-size: 17px; color: var(--ink); }

  .contacts {
    position: absolute; left: 330px; top: 104px;
    list-style: none;
    font-family: "Crimson Text", serif;
    color: var(--ink);
    font-size: 15px;
  }
  .contacts__item { display: flex; align-items: center; gap: 10px; height: 28px; white-space: nowrap; }
  .contacts__item--phone { font-size: 18px; }
  .contacts__icon { width: 16px; height: 16px; flex: none; }
</style>
</head>
<body>
<main class="stage">

  <section class="card card--front" aria-label="Business card front">
    <div class="brand">
      <h1 class="brand__name">Tova Brisk<br>Fitness Coaching</h1>
      <p class="brand__role">Personal Trainer</p>
    </div>
    <div class="action-photo" role="img" aria-label="Photo of the trainer in a pink top doing a wide leg stretch"></div>
    <div class="front-band"></div>
  </section>

  <section class="card card--back" aria-label="Business card back">
    <svg class="back-shapes" width="560" height="320" viewBox="0 0 560 320" aria-hidden="true">
      <polygon points="300,0 560,0 560,24" fill="var(--mint)"/>
      <polygon points="70,0 300,0 560,24 560,58" fill="var(--pink)"/>
      <polygon points="0,252 560,226 560,248 0,292" fill="var(--pink)"/>
      <polygon points="0,292 560,248 560,320 0,320" fill="var(--mint)"/>
    </svg>

    <div class="portrait" role="img" aria-label="Round portrait photo of the trainer"></div>

    <div class="identity">
      <h2 class="identity__name">Tova Penrick</h2>
      <p class="identity__role">Personal Trainer</p>
    </div>

    <ul class="contacts">
      <li class="contacts__item contacts__item--phone">
        <svg class="contacts__icon" viewBox="0 0 16 16" aria-hidden="true"><path d="M3.5 1.5l2.5 0.5 1 3-1.6 1.2c0.8 1.8 2.1 3.1 3.9 3.9L10.5 8.5l3 1 0.5 2.5-1.8 1.8C7 13.5 2.5 9 1.7 3.3z" fill="var(--ink)"/></svg>
        <span>07500 918 243</span>
      </li>
      <li class="contacts__item">
        <svg class="contacts__icon" viewBox="0 0 16 16" aria-hidden="true"><rect x="1" y="3.5" width="14" height="9" fill="none" stroke="var(--ink)" stroke-width="1.2"/><path d="M1 3.5l7 5 7-5" fill="none" stroke="var(--ink)" stroke-width="1.2"/></svg>
        <span>tova.penrick@mailgrove.net</span>
      </li>
      <li class="contacts__item">
        <svg class="contacts__icon" viewBox="0 0 16 16" aria-hidden="true"><rect x="2" y="2" width="12" height="12" fill="none" stroke="var(--ink)" stroke-width="1.4"/></svg>
        <span>snapgrid/Tova Brisk</span>
      </li>
    </ul>
  </section>

</main>
</body>
</html>
```